Blind Rivet Product catalogue

Need a design in wordpress with a productcatalogue where i present all products. This is a B2B business. The products is Blindrivets and Blindrivet nuts and accessories to this. I only want the basic information and also technical specification.

This is a subcompany to my existing company k7.m9.se but specializing in a subcategory

Target Market(s)

Businesses using blind rivet technology.

Industry/Entity Type

Industrial

Coding

Coded - Design and coding required

Number of Pages Required

5+ page

Font styles to use
Sans Serif

Requirements
Must have
• Three different categories for the products; Blind Rivets - Blind Rivet Nut - Riveting Tools
Nice to have
• Possible to ad login for more information of the different sizes

```html
<!DOCTYPE html>
<html lang="en">
<head>
<meta charset="utf-8">
<title>Blind Rivet Catalogue – Home</title>
<link rel="stylesheet" href="https://fonts.googleapis.com/css2?family=Jost:wght@300;400;500;700&display=swap">
<style>
:root{
  --topbar:#c5cffc;
  --teal:#72c0c2;
  --teal-dark:#5fb3b5;
  --ink:#111111;
  --ink-soft:#222222;
  --white:#ffffff;
  --footer:#2e569d;
  --footer-nav:#0d1836;
  --card-shadow:rgba(0,0,0,.28);
}
*{box-sizing:border-box;margin:0;padding:0}
html,body{width:750px;height:1200px;overflow:hidden;background:var(--white)}
body{position:relative;font-family:"Jost",sans-serif;color:var(--ink)}
.abs{position:absolute}

/* top contact bar */
.topbar{left:0;top:0;width:750px;height:42px;background:var(--topbar)}
.topbar-item{top:12px;font-size:13px;font-weight:300;white-space:nowrap}
.topbar-item b{font-weight:700}
.login{left:562px;top:0;width:121px;height:42px;background:var(--teal);border-radius:3px;
  display:flex;align-items:center;justify-content:center;gap:10px;font-weight:700;font-size:14px;letter-spacing:.3px}

/* header */
.brand{left:78px;top:60px;font-size:18px;font-weight:700;line-height:20px;letter-spacing:.5px}
.nav a{position:absolute;font-size:13px;font-weight:700;letter-spacing:.6px;color:var(--ink);text-decoration:none;white-space:nowrap}
.nav a.active{color:var(--teal)}
.cursor{width:16px;height:24px}

/* hero */
.hero{left:0;top:113px;width:750px;height:426px;
  background:
    linear-gradient(160deg,rgba(255,255,255,0) 40%,rgba(235,238,250,.85) 100%),
    linear-gradient(100deg,#5b63d6 0%,#7f88dd 35%,#8aa6d8 60%,#55c2b7 100%)}
.hero-title{left:0;top:296px;width:750px;text-align:center;font-size:35px;font-weight:700;letter-spacing:.5px}
.hero-quote{left:100px;top:358px;width:550px;text-align:center;font-size:23px;font-weight:300;line-height:30px;color:var(--ink-soft)}

/* catalog */
.section-title{left:0;top:578px;width:750px;text-align:center;font-size:27px;font-weight:700;letter-spacing:1px}
.card{top:640px;width:173px;height:309px;background:var(--white);box-shadow:0 1px 4px var(--card-shadow)}
.card-media{position:absolute;left:8px;top:6px;width:157px;height:158px;border-radius:4px}
.media-tool{background:radial-gradient(circle at 50% 50%,#3a3d44 0%,#6b6f78 45%,#eef0f3 80%)}
.media-nut{background:radial-gradient(circle at 50% 50%,#c9ccd1 0%,#e4e6ea 50%,#ffffff 80%)}
.media-rivet{background:linear-gradient(135deg,#ffffff 15%,#d7d9dd 45%,#bfc2c7 55%,#ffffff 85%)}
.pill{position:absolute;left:21px;top:177px;width:131px;height:29px;border-radius:15px;
  display:flex;align-items:center;justify-content:center;font-size:17px;font-weight:700;letter-spacing:.3px}
.pill-filled{background:var(--teal)}
.pill-outline{border:3px solid var(--teal);background:var(--white)}
.card-text{position:absolute;left:8px;top:209px;width:157px;text-align:center;font-size:13.5px;font-weight:300;line-height:16.6px}

/* footer */
.footer{left:0;top:1004px;width:750px;height:196px;background:var(--footer);color:var(--white)}
.footer-line{font-size:13.5px;font-weight:400;white-space:nowrap}
.footer-brand{left:0;top:1066px;width:750px;text-align:center;font-size:18px;font-weight:700;line-height:20px;letter-spacing:.5px;color:var(--white)}
.footer-nav a{color:var(--footer-nav)}
.footer-nav a.active{color:var(--teal)}
</style>
</head>
<body>

<header>
  <div class="abs topbar"></div>
  <div class="abs topbar-item" style="left:77px"><b>Email Us:</b> sample@sample.com</div>
  <div class="abs topbar-item" style="left:308px"><b>Call Us:</b> 800-400-600</div>
  <a class="abs login" href="#login" style="color:var(--ink);text-decoration:none">
    <svg width="26" height="24" viewBox="0 0 26 24" aria-hidden="true">
      <path d="M12 2h11v20H12" fill="none" stroke="#111" stroke-width="3"/>
      <path d="M1 12h14M10 6l6 6-6 6" fill="none" stroke="#111" stroke-width="3"/>
    </svg>
    LOG IN
  </a>

  <div class="abs brand">YOUR LOGO<br>YOUR SLOGAN</div>
  <nav class="nav">
    <a class="active" href="#home" style="left:374px;top:71px">HOME</a>
    <a href="#catalog" style="left:442px;top:71px">CATALOG</a>
    <a href="#about" style="left:527px;top:71px">ABOUT US</a>
    <a href="#contact" style="left:613px;top:71px">CONTACT</a>
  </nav>
  <svg class="abs cursor" style="left:397px;top:83px" viewBox="0 0 16 24" aria-hidden="true">
    <path d="M1 1v18l5-4 4 8 3-1.5-4-8h6z" fill="#fff" stroke="#222" stroke-width="1.4" stroke-linejoin="round"/>
  </svg>
</header>

<section>
  <div class="abs hero" role="img" aria-label="Photo of metal facade panels joined by rivets, in blue and teal light"></div>
  <h1 class="abs hero-title">LOREM ISPUN</h1>
  <p class="abs hero-quote">"It is worth emphasizing that the progress of the strategic decision reveals the patterns of The Investment of Contextual Duplication"</p>
</section>

<section id="catalog">
  <h2 class="abs section-title">OUR CATALOG</h2>

  <article class="abs card" style="left:91px">
    <div class="card-media media-tool" role="img" aria-label="Photo of a cordless riveting tool"></div>
    <div class="pill pill-filled">Riveting Tools</div>
    <p class="card-text">"Alas, the lack of knowledge of any set of system properties gives an overview of The Network of Superficial Indicator"</p>
  </article>

  <article class="abs card" style="left:288px">
    <div class="card-media media-nut" role="img" aria-label="Photo of a knurled steel blind rivet nut"></div>
    <div class="pill pill-outline">Blind Rivet Nut</div>
    <p class="card-text">"Alas, the lack of knowledge of any set of system properties gives an overview of The Network of Superficial Indicator"</p>
  </article>

  <article class="abs card" style="left:484px">
    <div class="card-media media-rivet" role="img" aria-label="Photo of a steel blind rivet"></div>
    <div class="pill pill-outline">Blind Rivets</div>
    <p class="card-text">"Alas, the lack of knowledge of any set of system properties gives an overview of The Network of Superficial Indicator"</p>
  </article>

  <svg class="abs cursor" style="left:237px;top:842px" viewBox="0 0 16 24" aria-hidden="true">
    <path d="M1 1v18l5-4 4 8 3-1.5-4-8h6z" fill="#fff" stroke="#222" stroke-width="1.4" stroke-linejoin="round"/>
  </svg>
</section>

<footer>
  <div class="abs footer"></div>
  <svg class="abs" style="left:75px;top:1042px" width="18" height="36" viewBox="0 0 18 36" aria-hidden="true">
    <path d="M9 1a8 8 0 0 0-8 8c0 7 8 26 8 26s8-19 8-26a8 8 0 0 0-8-8z" fill="#000"/>
    <circle cx="9" cy="9" r="3.4" fill="none" stroke="#fff" stroke-width="1.8"/>
  </svg>
  <div class="abs footer-line" style="left:106px;top:1047px">YOUR ADRESS</div>
  <div class="abs footer-line" style="right:69px;top:1039px">YOUR COMPANY E-MAIL</div>
  <div class="abs footer-brand">YOUR LOGO<br>YOUR SLOGAN</div>
  <nav class="nav footer-nav">
    <a class="active" href="#home" style="left:227px;top:1127px">HOME</a>
    <a href="#catalog" style="left:295px;top:1127px">CATALOG</a>
    <a href="#about" style="left:380px;top:1127px">ABOUT US</a>
    <a href="#contact" style="left:466px;top:1127px">CONTACT</a>
  </nav>
  <svg class="abs cursor" style="left:250px;top:1140px" viewBox="0 0 16 24" aria-hidden="true">
    <path d="M1 1v18l5-4 4 8 3-1.5-4-8h6z" fill="#fff" stroke="#222" stroke-width="1.4" stroke-linejoin="round"/>
  </svg>
  <div class="abs footer-line" style="left:75px;top:1166px">Design by YOUR COMPANY NAME</div>
</footer>

</body>
</html>
```